Whitcombe Framing Works - Card Design

I am looking to use the logo designs that you already did for me to develop a business card. I would like the card to have a black background and be double sided. I want white and green logo and text. I have attached an inspiration photo of a look that I like. I would like to use the Vertical Logo attached to take up the full front side of the card. On the back where I have my name and information, I would like to have the horizontal logo or maybe even just the image of the 'A' and trees without the text. I am open, but I am looking for something clean and simple and I want the green to really pop! Additional files can be found under Design #: 40593216

Target Market(s)

Homeowners

Industry/Entity Type

Construction

Contact Information for Business Card

Name: Marcus Pellow, Title: Project Manager, Phone: 831.555.0147, Email: whitcombeframingworks@mailbarn.net, address: 418 Juniper Ln, Felton, CA 95092, Lic# 2046318

Colors
00AB8E
00BBA5
67D7C9
C6EFE9
E9F9F6

Requirements
Nice to have
• I would like to see the logos that I have already got from SketchHarbor, though I am open to new ones

```html
<!DOCTYPE html>
<html lang="en">
<head>
<meta charset="utf-8">
<title>Whitcombe Framing Works – Business Card</title>
<link rel="stylesheet" href="https://fonts.googleapis.com/css2?family=Open+Sans:wght@400;700&display=swap">
<style>
  :root {
    --stage: #4a4a4a;
    --card-black: #141414;
    --green: #3fa84a;
    --green-light: #6fbb44;
    --white: #ffffff;
  }
  * { margin: 0; padding: 0; box-sizing: border-box; }
  html, body { width: 1200px; height: 801px; overflow: hidden; }
  body {
    background: var(--stage);
    font-family: "Open Sans", Arial, sans-serif;
    color: var(--white);
    position: relative;
  }
  .card {
    position: absolute;
    top: 246px;
    width: 540px;
    height: 309px;
    background: var(--card-black);
    overflow: hidden;
    border-bottom: 3px solid var(--green-light);
  }
  .card--info { left: 30px; }
  .card--brand { left: 630px; }

  .card__swoosh { position: absolute; inset: 0; width: 540px; height: 309px; }

  /* brand name blocks */
  .brand-name {
    font-weight: 700;
    color: var(--white);
    text-transform: uppercase;
    letter-spacing: 1px;
    line-height: 1.1;
  }
  .brand-main {
    position: absolute; left: 250px; top: 40px;
    font-size: 22px; width: 170px;
  }
  .brand-mini {
    position: absolute; left: 22px; top: 40px;
    width: 92px; height: 92px;
    border: 2px solid var(--white); border-radius: 50%;
    display: flex; align-items: center; justify-content: center; text-align: center;
  }
  .brand-mini .brand-name { font-size: 10px; }

  .address {
    position: absolute; left: 430px; top: 58px;
    font-size: 13px; line-height: 1.4;
  }
  .license {
    position: absolute; right: 22px; top: 150px;
    font-size: 13px;
  }

  .contact { position: absolute; left: 170px; top: 205px; }
  .contact__name { font-size: 22px; font-weight: 700; line-height: 1.1; }
  .contact__title { font-size: 14px; margin-bottom: 8px; }
  .contact__line { font-size: 13px; display: flex; align-items: center; gap: 7px; line-height: 1.55; }
  .contact__line svg { width: 12px; height: 12px; flex: none; }

  .brand-seal {
    position: absolute; left: 160px; top: 44px;
    width: 220px; height: 220px;
    border: 5px solid var(--white); border-radius: 50%;
    display: flex; align-items: center; justify-content: center; text-align: center;
  }
  .brand-seal .brand-name { font-size: 28px; }
</style>
</head>
<body>

  <section class="card card--info" aria-label="Card contact side">
    <svg class="card__swoosh" viewBox="0 0 540 309" aria-hidden="true">
      <path d="M120 309 C200 210 360 200 540 110 L540 309 Z" fill="var(--green)"/>
      <path d="M110 309 C190 200 350 185 520 110 C360 195 210 215 120 309 Z" fill="var(--green-light)"/>
    </svg>

    <div class="brand-mini"><span class="brand-name">Whitcombe Framing Works</span></div>
    <div class="brand-main brand-name">Whitcombe Framing Works</div>

    <p class="address">418 Juniper Ln,<br>Felton, CA 95092</p>
    <p class="license">License# 2046318</p>

    <div class="contact">
      <p class="contact__name">Marcus Pellow</p>
      <p class="contact__title">Project Manager</p>
      <p class="contact__line">
        <svg viewBox="0 0 24 24" aria-hidden="true"><path fill="#fff" d="M6.6 10.8a15 15 0 0 0 6.6 6.6l2.2-2.2a1 1 0 0 1 1-.25 11.4 11.4 0 0 0 3.6.57 1 1 0 0 1 1 1V20a1 1 0 0 1-1 1A17 17 0 0 1 3 4a1 1 0 0 1 1-1h3.5a1 1 0 0 1 1 1c0 1.25.2 2.45.57 3.57a1 1 0 0 1-.25 1z"/></svg>
        831.555.0147
      </p>
      <p class="contact__line">
        <svg viewBox="0 0 24 24" aria-hidden="true"><path fill="#fff" d="M2 5h20v14H2z M2 5l10 8 10-8" stroke="#3fa84a" stroke-width="1.5"/></svg>
        whitcombeframingworks@mailbarn.net
      </p>
    </div>
  </section>

  <section class="card card--brand" aria-label="Card brand side">
    <div class="brand-seal"><span class="brand-name">Whitcombe<br>Framing<br>Works</span></div>
  </section>

</body>
</html>
```